Web Design Project for Copperleaf Systems Collective

Design a webpage to replace www.copperleafsystemscollective.com.au

View the website and design a new website based on the same philosophy of the original.

The website will be fresh, simple, elegant, modern, and a hint of high degree of technical backdrop.

Please utilise the logo in the website design and keep the different contents.

Industry/Entity Type

Group

Requirements
Must have
• Must incorporate the logo which will be uploaded.

```html
<!DOCTYPE html>
<html lang="en">
<head>
<meta charset="utf-8">
<title>Copperleaf Systems Collective</title>
<link rel="stylesheet" href="https://fonts.googleapis.com/css2?family=Open+Sans:wght@400;600&family=Roboto+Condensed:wght@400;700&family=Gelasio:wght@400&family=Hind:wght@400;500&display=swap">
<style>
:root{
  --navy:#2419a4;
  --navy-deep:#1d1590;
  --heading:#1d2a8e;
  --link:#1b5c9e;
  --yellow:#fcc21f;
  --yellow-deep:#f5a713;
  --hero-bg:#f8f5f2;
  --text:#5f5f5f;
  --blue:#1a8cc7;
  --blue-deep:#10659f;
  --red:#d8261b;
  --white:#fff;
}
*{box-sizing:border-box;margin:0;padding:0}
html,body{width:857px;height:1200px;overflow:hidden;background:var(--white)}
.page{position:relative;width:857px;height:1200px;overflow:hidden;font-family:"Open Sans",sans-serif}

/* header */
.header{position:absolute;left:0;top:0;width:857px;height:136px;background:var(--white)}
.world-map{position:absolute;left:493px;top:0;width:364px;height:136px;
  background:radial-gradient(ellipse at 60% 40%,rgba(150,150,230,.55),rgba(190,190,240,.25) 55%,rgba(255,255,255,0) 75%)}
.brand{position:absolute;left:37px;top:30px;display:flex;align-items:center;gap:10px}
.brand-mark{width:44px;height:44px;border-radius:50%;background:var(--navy-deep)}
.brand-name{font-family:"Hind",sans-serif;font-weight:400;font-size:22px;line-height:24px;color:var(--navy-deep);width:190px}

/* nav */
.nav{position:absolute;left:0;top:136px;width:857px;height:45px;background:linear-gradient(#2a1fb5,var(--navy-deep));display:flex}
.nav a{display:flex;align-items:center;justify-content:center;color:var(--white);text-decoration:none;font-size:11.5px;text-transform:uppercase;border-left:1px solid rgba(255,255,255,.15)}
.nav a.active{background:linear-gradient(#ffd33a,var(--yellow-deep));color:#222;border-left:none}

/* hero */
.hero{position:absolute;left:0;top:181px;width:857px;height:323px;background:var(--hero-bg)}
.hero-shadow{position:absolute;left:40px;top:500px;width:800px;height:12px;border-radius:50%;background:radial-gradient(ellipse,rgba(0,0,0,.18),rgba(0,0,0,0) 70%)}
.solution-list{position:absolute;left:43px;top:22px;list-style:none}
.solution{margin-bottom:14px}
.solution-title{display:flex;align-items:center;gap:7px;font-family:"Hind",sans-serif;font-size:21px;color:var(--heading);height:30px}
.solution-num{width:29px;height:29px;border-radius:50%;background:radial-gradient(circle at 40% 35%,#f0584a,var(--red));color:var(--white);font-family:"Roboto Condensed",sans-serif;font-weight:700;font-size:19px;display:flex;align-items:center;justify-content:center;border:2px solid #fff;box-shadow:0 1px 2px rgba(0,0,0,.3)}
.solution-items{list-style:none;margin-left:62px;margin-top:4px}
.solution-items li{font-size:12.5px;color:var(--link);height:23px;display:flex;align-items:center;gap:8px}
.solution-items li::before{content:"";border-left:5px solid var(--link);border-top:4px solid transparent;border-bottom:4px solid transparent}

.slider{position:absolute;left:332px;top:23px;width:508px;height:271px;background:var(--white);padding:6px;box-shadow:0 2px 6px rgba(0,0,0,.35)}
.slide-photo{position:relative;width:100%;height:100%;background:linear-gradient(120deg,#4a3a30,#8b7a6c 45%,#c9bdb1 70%,#6d5f55)}
.slide-title{position:absolute;left:16px;top:8px;color:var(--white);font-family:"Roboto Condensed",sans-serif;font-weight:700;font-size:38px;line-height:40px}
.slide-sub{position:absolute;left:18px;top:48px;color:var(--white);font-size:13px}
.slider-arrow{position:absolute;top:316px;width:45px;height:53px}
.slider-arrow.prev{left:325px}
.slider-arrow.next{left:802px}

/* content */
.content{position:absolute;left:11px;top:512px;width:608px;height:606px;background:linear-gradient(90deg,#f6f6f6,#fbfbfb 40%,#f8f8f8)}
.welcome{position:absolute;left:10px;top:14px;font-family:"Gelasio",serif;color:var(--heading);font-weight:400}
.welcome small{font-size:16px;color:#333}
.welcome span{font-size:26px}
.welcome-rule{position:absolute;left:10px;top:52px;width:560px;height:1px;background:linear-gradient(90deg,#ddd,rgba(221,221,221,0))}
.copy{position:absolute;left:10px;top:69px;width:566px;font-family:"Gelasio",serif;font-size:12.2px;line-height:15.5px;color:var(--text)}
.copy p{margin-bottom:15.5px}
.values{list-style:none;margin:22px 0 30px 22px}
.values li{color:var(--heading);height:22px;display:flex;align-items:center;gap:10px}
.values li::before{content:"";border-left:5px solid var(--heading);border-top:4px solid transparent;border-bottom:4px solid transparent}

/* sidebar */
.quote-box{position:absolute;left:634px;top:525px;width:207px;height:245px;border-radius:6px;background:linear-gradient(var(--blue),var(--blue-deep))}
.quote-title{position:absolute;left:-5px;top:8px;width:217px;height:34px;background:var(--navy-deep);color:var(--white);font-family:"Open Sans",sans-serif;font-weight:600;font-size:17px;display:flex;align-items:center;justify-content:center;box-shadow:0 2px 3px rgba(0,0,0,.3)}
.field{position:absolute;left:10px;width:187px;background:var(--white);border:1px solid #cde;font-size:9px;color:#999;padding:4px 6px}
.btn{position:absolute;display:flex;align-items:center;gap:8px;padding:0 8px 0 12px;height:31px;border-radius:7px;color:var(--white);font-weight:600;font-size:15px;letter-spacing:.3px}
.btn-yellow{left:10px;top:206px;width:108px;background:linear-gradient(#ffd84a,var(--yellow-deep))}
.btn-navy{left:12px;top:101px;width:108px;background:linear-gradient(#3a2fc5,var(--navy-deep))}

.newsletter{position:absolute;left:634px;top:783px;width:207px;height:140px;border-radius:6px;background:linear-gradient(#ffd54a,var(--yellow));box-shadow:0 1px 3px rgba(0,0,0,.2)}
.newsletter h2{position:absolute;left:12px;top:8px;font-family:"Roboto Condensed",sans-serif;font-weight:400;font-size:19px;color:#222}
.newsletter h2 b{font-weight:700}
.newsletter p{position:absolute;left:12px;top:44px;font-size:11.5px;color:#222}

.call-us{position:absolute;left:634px;top:937px;width:207px;height:183px;border-radius:6px;background:linear-gradient(var(--blue),var(--blue-deep));color:var(--white)}
.call-us h2{position:absolute;left:12px;top:8px;font-family:"Roboto Condensed",sans-serif;font-weight:400;font-size:20px}
.call-us-rule{position:absolute;left:0;top:39px;width:207px;height:1px;background:rgba(255,255,255,.3)}
.call-us address{position:absolute;left:13px;top:47px;font-style:normal;font-family:"Gelasio",serif;font-size:12px;line-height:16.5px}
.call-us b{color:#111;font-weight:400}

/* footer */
.footer{position:absolute;left:0;top:1134px;width:857px;height:66px;background:var(--navy);color:var(--white);text-align:center;font-size:9px}
.footer-links{margin-top:18px;display:flex;justify-content:center;gap:0}
.footer-links a{color:var(--white);text-decoration:none;padding:0 8px;border-left:1px solid rgba(255,255,255,.8);line-height:10px}
.footer-links a:first-child{border-left:none}
.footer-copy{margin-top:4px}
</style>
</head>
<body>
<div class="page">

  <header class="header">
    <div class="world-map" role="img" aria-label="Faint world map in soft violet"></div>
    <div class="brand">
      <span class="brand-mark"></span>
      <span class="brand-name">Copperleaf Systems Collective</span>
    </div>
  </header>

  <nav class="nav">
    <a class="active" style="width:88px">Home</a>
    <a style="width:103px">Mission</a>
    <a style="width:109px">Services</a>
    <a style="width:117px">Products</a>
    <a style="width:113px">Partners</a>
    <a style="width:92px">Blog</a>
    <a style="width:131px">Online Shop</a>
    <a style="width:104px">Contact</a>
  </nav>

  <section class="hero">
    <ol class="solution-list">
      <li class="solution">
        <div class="solution-title"><span class="solution-num">1</span>Security</div>
        <ul class="solution-items"><li>Access Control</li><li>Monitoring</li></ul>
      </li>
      <li class="solution">
        <div class="solution-title"><span class="solution-num">2</span>Communications</div>
        <ul class="solution-items"><li>DECT Phones</li><li>Pagers</li><li>Intercomms</li></ul>
      </li>
      <li class="solution">
        <div class="solution-title"><span class="solution-num">3</span>Nurse Call</div>
        <ul class="solution-items"><li>Integrated Communications</li><li>Patient Monitoring</li></ul>
      </li>
    </ol>
    <div class="slider">
      <div class="slide-photo" role="img" aria-label="Photo of a wall-mounted security camera">
        <div class="slide-title">CCTV</div>
        <div class="slide-sub">an IP Cameras</div>
      </div>
    </div>
  </section>

  <svg class="slider-arrow prev" viewBox="0 0 45 53" aria-hidden="true">
    <rect x="1" y="1" width="43" height="49" rx="6" fill="#1487cf" stroke="#0b5f9a"/>
    <path d="M14 26 L30 15 L30 37 Z" fill="#0d3e73"/>
  </svg>
  <svg class="slider-arrow next" viewBox="0 0 45 53" aria-hidden="true">
    <rect x="1" y="1" width="43" height="49" rx="6" fill="#1487cf" stroke="#0b5f9a"/>
    <path d="M31 26 L15 15 L15 37 Z" fill="#0d3e73"/>
  </svg>
  <div class="hero-shadow"></div>

  <main class="content">
    <h1 class="welcome"><small>welcome to </small><span>Copperleaf Systems Collective</span></h1>
    <div class="welcome-rule"></div>
    <div class="copy">
      <p>Copperleaf Systems Collective provides products and services through an integrated approach for reliable, mature and flexible solutions. Solutions that provide scale from single business premise to multinational offices through-out the world. We understand solutions need to be tailored to your needs; we keep in mind your growth in the years to come.</p>
      <p>Allow us the opportunity to unify your network...</p>
      <p>Traditionally when you as a customer required a range of electrical and communication solutions, you would have to go through different service providers to match your specifications. Some organisations hire Electrical Engineering Consultants, taking the complexity out of the initial project design. This model was effective in the project however does not continue once the solution has been provided and the consultant moves on to the next project. This approach tendered towards a once-off project based scope.</p>
      <p>Alternatively you may choose to complete the project in-house, allowing you to engage and "project manage" the suppliers to work with each other. Whilst some may enjoy this new challenge, most businesses face a lack of resources when managing non-core business activities. This would most likely require you to open up a new IT and communications department for this challenge and an understanding of technologies needed and how each electrical and communication systems integrate.</p>
      <p>Here at Copperleaf Systems Collective, we wish to offer you a leaner approach.</p>
      <p>We are an Electrical Engineering consulting company specialising in consultation, supply, installation and service of electrical and communications systems. From design to implementation and continuing service management, we assist in managing your solution as you grow. By offering a unified network of goods and service providers, the quality of your electrical and communication solutions become integrated from the very first design through to future service management requirements.</p>
      <ul class="values">
        <li>Unified in collaborations.</li>
        <li>Unified in solutions.</li>
        <li>Copperleaf Systems Collective by nature.</li>
      </ul>
      <p>Let us Unify your electrical and communication solutions</p>
    </div>
  </main>

  <aside class="quote-box">
    <div class="quote-title">GET A FREE QUOTE</div>
    <div class="field" style="top:50px;height:19px">Tyep Your Name</div>
    <div class="field" style="top:78px;height:19px">Type Your email id</div>
    <div class="field" style="top:109px;height:85px">Type your requirements</div>
    <div class="btn btn-yellow">SUBMIT
      <svg width="22" height="22" viewBox="0 0 22 22" aria-hidden="true"><circle cx="11" cy="11" r="9" fill="none" stroke="#fff" stroke-width="2"/><path d="M7 11h7M11 7.5l3.5 3.5L11 14.5" fill="none" stroke="#fff" stroke-width="2"/></svg>
    </div>
  </aside>

  <aside class="newsletter">
    <h2><b>FREE</b> Newsletter!</h2>
    <p>Fill the form to get FREE UPDATE</p>
    <div class="field" style="left:12px;top:70px;width:184px;height:20px;border-color:#555">Type your email id</div>
    <div class="btn btn-navy">SUBMIT
      <svg width="22" height="22" viewBox="0 0 22 22" aria-hidden="true"><circle cx="11" cy="11" r="9" fill="none" stroke="#fff" stroke-width="2"/><path d="M7 11h7M11 7.5l3.5 3.5L11 14.5" fill="none" stroke="#fff" stroke-width="2"/></svg>
    </div>
  </aside>

  <aside class="call-us">
    <h2>Call Us</h2>
    <div class="call-us-rule"></div>
    <address>
      CSC PTY. LTD.<br>
      ACN: <b>482 615 093</b><br>
      ABN: <b>36 482 615 093</b><br>
      FAX: <b>+61 2 9044 3187</b><br>
      Mail:<br>
      P.O.Box 318 Glebe, NSW,<br>
      Australia 2037
    </address>
  </aside>

  <footer class="footer">
    <div class="footer-links">
      <a>Home</a><a>Mission</a><a>Services</a><a>Products</a><a>Partners</a><a>Blog</a><a>Online Shop</a><a>Contact</a>
    </div>
    <div class="footer-copy">© Copperleaf Systems Collective Pty Ltd. All Rights Reserved</div>
  </footer>

</div>
</body>
</html>
```